Real Estate Team Needs Business Cards

Double sided - Team Member on Front, Team Leader on Back (back side will contain more details).
Colors to use:
Red = R: 233 G: 1 B: 2
Grey = R: 89 G: 89 B: 89
Black= R: 0 B: 0 B: 0
** MAIN FOCUS ** ( separate border, color, design, etc. to really stand out - whatever you think draws the most attention ) on both sides for "Sell for 1%‡" and "Buy & receive up to a 1% rebate‡". Must have fine print **
**Please make both sides stand out and look unique / different
Business card to have round corners (standard size 3.5" x 2").:
Document Trim Size
89 x 51 mm
1050 x 600 pixels
Full Bleed Size
92 x 54 mm
1085 x 635 pixels
Basic example provided. Please redesign as you see best. In your design - Please use the same picture on both sides. Name, address, phone number, email, etc. will be provided to the selected design. QR code on back side only if there is room (not important)

```html
<!DOCTYPE html>
<html lang="en">
<head>
<meta charset="utf-8">
<title>Summit Key Realty – Business Cards</title>
<link rel="stylesheet" href="https://fonts.googleapis.com/css2?family=Roboto:wght@400;500;700;900&display=swap">
<style>
  :root {
    --red: #e90102;
    --grey: #595959;
    --black: #000000;
    --paper: #fafafa;
    --backdrop: #e9e6e2;
    --photo-top: #c9cbcd;
    --photo-bottom: #2f4a8a;
  }
  * { box-sizing: border-box; margin: 0; padding: 0; }
  html, body { width: 1200px; height: 960px; overflow: hidden; }
  body {
    background: var(--backdrop);
    font-family: "Roboto", Arial, sans-serif;
    color: var(--black);
    position: relative;
  }
  .card {
    position: absolute;
    left: 250px;
    width: 700px;
    height: 400px;
    background: var(--paper);
    border-radius: 14px;
    box-shadow: 0 6px 18px rgba(0,0,0,.18);
    overflow: hidden;
  }
  .card--front { top: 60px; }
  .card--back { top: 500px; }

  .brand {
    position: absolute;
    display: flex;
    align-items: center;
    gap: 10px;
    font-weight: 900;
    font-size: 26px;
    letter-spacing: .5px;
    color: var(--black);
    text-transform: uppercase;
    white-space: nowrap;
  }
  .brand__mark { width: 16px; height: 16px; background: var(--red); }
  .brand-rule {
    position: absolute;
    height: 2px;
    background: var(--red);
  }

  .offers { position: absolute; list-style: none; }
  .offers li {
    display: flex; align-items: center; gap: 8px;
    color: var(--red); font-weight: 700; font-size: 17px; line-height: 24px;
  }
  .offers svg { width: 16px; height: 12px; flex: none; }

  .services { position: absolute; list-style: none; font-size: 16px; line-height: 22px; color: var(--black); }

  .name {
    position: absolute; color: var(--red); font-weight: 900; white-space: nowrap;
  }
  .position { position: absolute; font-size: 18px; color: var(--black); }
  .visit { position: absolute; font-size: 16px; color: var(--black); white-space: nowrap; }

  .address { position: absolute; left: 48px; top: 70px; font-size: 16px; line-height: 22px; }
  .address__label { color: var(--red); font-weight: 500; }

  .contacts { position: absolute; list-style: none; font-size: 16px; line-height: 24px; }
  .contacts li { display: flex; align-items: center; gap: 8px; white-space: nowrap; }
  .contacts svg { width: 14px; height: 14px; flex: none; }

  .portrait {
    position: absolute;
    border-radius: 50%;
    border: 4px solid var(--red);
    background: linear-gradient(180deg, var(--photo-top) 0%, var(--photo-top) 55%, var(--photo-bottom) 100%);
  }
</style>
</head>
<body>

<!-- Front: team member -->
<section class="card card--front">
  <div class="address">
    <p class="address__label">Address:</p>
    <p>Calle Olmo Verde 14,<br>18600 - Motril, Granada, Spain.</p>
    <ul class="contacts" style="position:static;margin-top:2px;">
      <li><svg viewBox="0 0 16 16"><path fill="var(--red)" d="M3 1l3 3-1.5 2a9 9 0 005 5L11.5 9.5l3 3-2 2.5C6 14 2 10 1 3z"/></svg>555-014-2288</li>
      <li><svg viewBox="0 0 16 16"><rect x="1" y="3" width="14" height="10" fill="var(--red)"/><path d="M1 3l7 6 7-6" stroke="#fff" stroke-width="1.5" fill="none"/></svg>hello@samplemail.com</li>
    </ul>
  </div>
  <div class="portrait" style="left:130px;top:205px;width:170px;height:170px;" role="img" aria-label="Portrait photo of the agent in a navy suit"></div>

  <div class="brand" style="left:360px;top:40px;"><span class="brand__mark"></span>Summit Key Realty</div>
  <div class="brand-rule" style="left:360px;top:82px;width:290px;"></div>

  <ul class="offers" style="left:380px;top:112px;">
    <li><svg viewBox="0 0 16 12"><path fill="var(--red)" d="M0 4h9V0l7 6-7 6V8H0z"/></svg>Sell for 1%</li>
    <li><svg viewBox="0 0 16 12"><path fill="var(--red)" d="M0 4h9V0l7 6-7 6V8H0z"/></svg>Buy &amp; receive up to a 1% rebate</li>
  </ul>
  <ul class="services" style="left:404px;top:166px;">
    <li>Free home evalution</li>
    <li>Free local sold reports</li>
    <li>Advanced Property Search</li>
  </ul>
  <p class="name" style="left:404px;top:240px;font-size:28px;">Daniel Hartwell</p>
  <p class="position" style="left:420px;top:278px;">Position</p>
  <p class="visit" style="left:420px;top:302px;">Visit www.yoursite.com for details</p>
</section>

<!-- Back: team leader -->
<section class="card card--back">
  <p class="name" style="left:56px;top:70px;font-size:32px;">Daniel Hartwell</p>
  <p class="position" style="left:150px;top:112px;">Position</p>
  <div class="portrait" style="left:150px;top:170px;width:195px;height:195px;" role="img" aria-label="Portrait photo of the team leader in a navy suit"></div>

  <div class="brand" style="left:380px;top:40px;"><span class="brand__mark"></span>Summit Key Realty</div>
  <div class="brand-rule" style="left:380px;top:82px;width:290px;"></div>

  <ul class="offers" style="left:410px;top:150px;">
    <li><svg viewBox="0 0 16 12"><path fill="var(--red)" d="M0 4h9V0l7 6-7 6V8H0z"/></svg>Sell for 1%</li>
    <li><svg viewBox="0 0 16 12"><path fill="var(--red)" d="M0 4h9V0l7 6-7 6V8H0z"/></svg>Buy &amp; receive up to a 1% rebate</li>
  </ul>
  <ul class="contacts" style="left:434px;top:206px;">
    <li><svg viewBox="0 0 16 16"><rect x="4" y="1" width="8" height="14" rx="1.5" fill="none" stroke="var(--red)" stroke-width="1.6"/></svg>555-014-2288</li>
    <li><svg viewBox="0 0 16 16"><path fill="var(--red)" d="M3 1l3 3-1.5 2a9 9 0 005 5L11.5 9.5l3 3-2 2.5C6 14 2 10 1 3z"/></svg>555-014-2288</li>
    <li><svg viewBox="0 0 16 16"><rect x="1" y="3" width="14" height="10" fill="var(--red)"/><path d="M1 3l7 6 7-6" stroke="#fff" stroke-width="1.5" fill="none"/></svg>hello@samplemail.com</li>
  </ul>
  <p class="visit" style="left:434px;top:282px;">Visit www.yoursite.com for details</p>
</section>

</body>
</html>
```